Book cover - Quiet Rooms, Open Doors

Book cover for Ebook (Pagelight) and wrap around print cover (Printvale) (back, front, and spine)

The book title (may slightly change by end of brief):
(MAIN TITLE) 'Quiet Rooms, Open Doors'
(SUB HEADING) 'A Week-by-Week Practical Workbook to Loosen Nervous Habits, Quieten Doubt and Build Steady Poise'
by Dr Owen Hartley

I would like a bold, stand out cover. Contemporary. I would like to avoid stereotypical images of people looking anxious or worried. I would like the design to be more uplifting and hopeful, rather than focusing on the negative aspect of anxiety, but avoiding cliched photos of people raising their hands in the air, smiling and jumping etc. The cover should appeal to both men and women.

Trim size of book cover (for PrintVale) is 5.25" x 8" back and front with a spine size of 0.477 inches

Reason: I have decided to extend the deadline by 1 more day, not because I am unhappy with the quality of the designs, but because a few designers have contacted me to explain they have had technical difficulties when submitting their files. Thanks everyone for the hard work and great designs.

Target Market(s)

Males and females (16+) who struggle with social anxiety and shyness

Industry/Entity Type

Social

Font styles to use
Serif

Requirements
Must have
• Bold cover that is modern and contemporary. For example, I like these covers:
• http://shrtlnk.example/k4Tq9Zb
• http://shrtlnk.example/m8Wv2Hn
• http://shrtlnk.example/p3Jx6Lr
• http://shrtlnk.example/t7Gd1Qe
• http://shrtlnk.example/v2Nk8Fy
• http://shrtlnk.example/w9Bh4Cs
• http://shrtlnk.example/z5Mf3Ud
Nice to have
• Open to abstract designs.
Should not have
• No stereotypical pictures of people who look anxious or worried. Avoid cliched photos of people raising their hands in the air, smiling and jumping etc.

```html
<!DOCTYPE html>
<html lang="en">
<head>
<meta charset="utf-8">
<title>Quiet Rooms, Open Doors – Wrap Cover</title>
<link rel="stylesheet" href="https://fonts.googleapis.com/css2?family=Oswald:wght@500;700&family=Open+Sans:wght@400;600&family=Arimo:wght@400;700&display=swap">
<style>
  :root {
    --stage: #eceef0;
    --navy: #0d2a5a;
    --spine-edge: #0b2550;
    --blue-deep: #2aa3da;
    --blue-mid: #5cc0ea;
    --blue-light: #c4e9f7;
    --art-a: #7fd0f0;
    --art-b: #2b9fd8;
    --label: #fbfbf8;
  }
  * { margin: 0; padding: 0; box-sizing: border-box; }
  html, body { width: 1200px; height: 1200px; overflow: hidden; background: var(--stage); }
  .canvas { position: relative; width: 1200px; height: 1200px; }
  .wrap-cover {
    position: absolute; left: 51px; top: 200px;
    width: 1098px; height: 800px;
    display: flex;
    box-shadow: 0 10px 30px rgba(0,0,0,.12);
  }
  .panel { position: relative; width: 525px; height: 800px; overflow: hidden; }
  .back-cover { background: radial-gradient(ellipse 70% 60% at 45% 40%, var(--blue-light), var(--blue-mid) 60%, var(--blue-deep)); }
  .front-cover { background: radial-gradient(ellipse 65% 60% at 50% 55%, var(--blue-light), var(--blue-mid) 60%, var(--blue-deep)); }
  .spine {
    position: relative; width: 48px; height: 800px;
    background: linear-gradient(90deg, var(--spine-edge) 0 5px, var(--blue-deep) 5px 43px, var(--spine-edge) 43px);
    display: flex; flex-direction: column; align-items: center; justify-content: space-between;
    padding: 28px 0 24px;
  }
  .spine-title, .spine-author {
    writing-mode: vertical-rl;
    font-family: "Arimo", Arial, sans-serif; color: var(--navy);
  }
  .spine-title { font-weight: 700; font-size: 19px; letter-spacing: .3px; }
  .spine-author { font-weight: 400; font-size: 15px; }

  .author {
    position: absolute; top: 62px; left: 0; width: 100%;
    text-align: center; font-family: "Open Sans", sans-serif; font-weight: 400;
    font-size: 38px; color: var(--navy);
  }
  .title {
    position: absolute; top: 150px; left: 0; width: 100%; text-align: center;
    font-family: "Oswald", sans-serif; font-weight: 700; color: var(--navy);
    text-transform: uppercase; line-height: 1.02; letter-spacing: -.5px;
  }
  .title .line { display: block; font-size: 82px; }
  .front-art { position: absolute; left: 145px; top: 390px; width: 300px; height: 290px; }
  .subtitle {
    position: absolute; left: 50px; right: 50px; top: 690px; text-align: center;
    font-family: "Oswald", sans-serif; font-weight: 500; font-size: 20px; line-height: 1.25;
    color: var(--navy);
  }

  .back-art { position: absolute; left: 20px; top: 40px; width: 220px; height: 310px; }
  .back-title {
    position: absolute; right: 38px; top: 200px; text-align: right;
    font-family: "Oswald", sans-serif; font-weight: 700; color: var(--navy);
    text-transform: uppercase; font-size: 50px; line-height: 1.05;
  }
  .back-copy {
    position: absolute; left: 150px; right: 38px; top: 372px;
    font-family: "Open Sans", sans-serif; font-size: 12px; line-height: 1.4;
    color: var(--navy); text-align: justify;
  }
  .back-copy p + p { margin-top: 11px; }
  .barcode-area {
    position: absolute; right: 38px; bottom: 28px; width: 215px; height: 110px;
    background: var(--label);
  }
</style>
</head>
<body>
<div class="canvas">
  <div class="wrap-cover">
    <section class="panel back-cover">
      <svg class="back-art" role="img" aria-label="Light blue folded-paper bird in flight" viewBox="0 0 220 310">
        <defs>
          <linearGradient id="backArtFill" x1="0" y1="0" x2="1" y2="1">
            <stop offset="0" stop-color="var(--art-a)"/>
            <stop offset="1" stop-color="var(--art-b)"/>
          </linearGradient>
        </defs>
        <rect width="220" height="310" rx="18" fill="url(#backArtFill)" opacity=".55"/>
      </svg>
      <h2 class="back-title">Quiet Rooms,<br>Open<br>Doors</h2>
      <div class="back-copy">
        <p>The book title (may slightly change by end of brief): 'Quiet Rooms, Open Doors' (SUB HEADING) 'A Week-by-Week Practical Workbook to Loosen Nervous Habits, Quieten Doubt and Build Steady Poise' by Dr Owen Hartley</p>
        <p>I would like a bold, stand out cover. Contemporary. I would like to avoid stereotypical images of people looking anxious or worried. I would like the design to be more uplifting and hopeful, rather than focusing on the negative aspect of anxiety, but avoiding cliched photos of people raising their hands in the air, smiling and jumping etc. The cover should appeal to both men and women.</p>
        <p>Trim size of book cover (for PrintVale) is 5.25" x 8" back and front with a spine size of 0.477 inches</p>
      </div>
      <div class="barcode-area"></div>
    </section>

    <aside class="spine">
      <span class="spine-title">Quiet Rooms, Open Doors</span>
      <span class="spine-author">Dr Owen Hartley</span>
    </aside>

    <section class="panel front-cover">
      <p class="author">Dr Owen Hartley</p>
      <h1 class="title">
        <span class="line">Quiet Rooms,</span>
        <span class="line">Open Doors</span>
      </h1>
      <svg class="front-art" role="img" aria-label="Folded-paper bird flying free from an open white birdcage" viewBox="0 0 300 290">
        <defs>
          <linearGradient id="frontArtFill" x1="1" y1="0" x2="0" y2="1">
            <stop offset="0" stop-color="var(--art-a)"/>
            <stop offset="1" stop-color="var(--art-b)"/>
          </linearGradient>
        </defs>
        <rect width="300" height="290" rx="18" fill="url(#frontArtFill)" opacity=".55"/>
      </svg>
      <p class="subtitle">A Week-by-Week Practical Workbook to Loosen Nervous Habits, Quieten Doubt and Build Steady Poise</p>
    </section>
  </div>
</div>
</body>
</html>
```